Lawn Sign For Construction Projects - Vantor Power

This contest is for a lawn sign that will be placed in the front yard of recently completed construction projects. The goal here is to have a bold advertising sign that is visible from a vehicle driving past.

We are still deciding on the default size for our sign, we also may use multiple sizes. The two sizes we will more than likely be using are: 18"h x 24"w and 24"h x 36"w.

Preference will be given to designers that submit original designs that tie into our current brand and are either in both the size formats listed above or are easy to scale in photoshop or illustrator.

In the files, you will see our logo and an example of a lawn sign.

Please contact us with any questions or comments you may have!

Thank You,
- The Vantor Power Team

Industry/Entity Type

Residential Construction

Colors
34a7d8
ffffff
faa54b

Requirements
Nice to have
• 1. The sign must tie into our current branding and color scheme.
• 2. The sign must be clearly visible and readable.
• 3. The sign must include our phone number in readable print.
• 4. Our website written in small print along the bottom of the sign.
• 5. Must mention we install the following products:
• a.) Solar
• b.) Roofing
• c.) Windows
• d.) Artificial Lawn
• e.) Whole House Fans
• f.) Patio Covers

```html
<!DOCTYPE html>
<html lang="en">
<head>
<meta charset="utf-8">
<title>Vantor Power – Zero Upfront Lawn Sign</title>
<link rel="stylesheet" href="https://fonts.googleapis.com/css2?family=Archivo:wght@800&family=Montserrat:wght@600&family=Questrial&display=swap">
<style>
  :root {
    --page-bg: #e8eae6;
    --sign-black: #000000;
    --sign-blue: #1174bd;
    --sign-white: #ffffff;
    --headline-orange: #ee5726;
    --brand-orange: #f08a2a;
  }
  html, body {
    margin: 0;
    width: 1200px;
    height: 1200px;
    overflow: hidden;
    background: var(--page-bg);
  }
  .lawn-sign {
    position: absolute;
    left: 40px;
    top: 180px;
    width: 1120px;
    height: 840px;
    display: block;
  }
  .brand-name {
    font-family: "Montserrat", Arial, sans-serif;
    font-weight: 600;
    fill: var(--brand-orange);
  }
  .brand-dot { fill: none; stroke: var(--brand-orange); stroke-width: 9; }
  .headline {
    font-family: "Archivo", "Arial Black", sans-serif;
    font-weight: 800;
    fill: var(--headline-orange);
  }
  .phone {
    font-family: "Questrial", "Century Gothic", sans-serif;
    fill: var(--sign-white);
  }
  .website {
    font-family: "Questrial", "Century Gothic", sans-serif;
    fill: var(--sign-black);
  }
  .band-top { fill: var(--sign-black); }
  .band-bottom { fill: var(--sign-blue); }
  .oval { fill: var(--sign-white); }
</style>
</head>
<body>
<svg class="lawn-sign" viewBox="0 0 1120 840" xmlns="http://www.w3.org/2000/svg" role="img" aria-label="Vantor Power lawn sign: Zero Upfront">
  <rect class="band-top" x="0" y="0" width="1120" height="420"/>
  <rect class="band-bottom" x="0" y="420" width="1120" height="420"/>
  <ellipse class="oval" cx="560" cy="392" rx="563" ry="247"/>

  <circle class="brand-dot" cx="322" cy="86" r="50"/>
  <text class="brand-name" x="400" y="110" font-size="64" textLength="410" lengthAdjust="spacingAndGlyphs">VANTOR POWER</text>

  <text class="headline" x="560" y="346" font-size="212" text-anchor="middle" textLength="550" lengthAdjust="spacingAndGlyphs">Zero</text>
  <text class="headline" x="560" y="537" font-size="212" text-anchor="middle" textLength="904" lengthAdjust="spacingAndGlyphs">Upfront</text>

  <text class="phone" x="560" y="749" font-size="118" text-anchor="middle" textLength="814" lengthAdjust="spacingAndGlyphs">055 218 4630</text>
  <text class="website" x="560" y="816" font-size="44" text-anchor="middle" textLength="470" lengthAdjust="spacingAndGlyphs">www.vantorpower.com</text>
</svg>
</body>
</html>
```